Website that informs user about the Darknet

A short 1 pager website that explains what the darknet is.
Current site: https://velorimo.gs/ & https://quanteph.kr/. No logo needed. Just an informational page. Choose the layout / colours that you prefer.

Target Market(s)

Endusers, companies etc.

Coding

Coded - Design and coding required

Number of Pages Required

1 page

Requirements
Must have
• 1 Small contact form - thats all
Should not have
• The page must look professional. Not for kids. I target mainly adults / employees

```html
<!DOCTYPE html>
<html lang="en">
<head>
<meta charset="utf-8">
<title>Darknet and Dark Web</title>
<link href="https://fonts.googleapis.com/css2?family=Barlow+Condensed:wght@500;600&family=Barlow:wght@500;600;700&family=Open+Sans:wght@400;600&display=swap" rel="stylesheet">
<style>
:root{
  --ink:#14161b;
  --night:#0b0d12;
  --night-2:#12151c;
  --text:#5b5f66;
  --muted:#8a8f97;
  --rule:#d9dbdf;
  --accent:#f2b705;
  --link:#2a6bd1;
  --paper:#ffffff;
  --soft:#f3f4f6;
}
*{box-sizing:border-box;margin:0;padding:0}
html,body{width:1200px;height:5196px;overflow:hidden;background:var(--paper)}
body{font-family:"Open Sans",Arial,sans-serif;color:var(--text);font-size:13px;line-height:1.75}
h1,h2,.display{font-family:"Barlow Condensed","Arial Narrow",sans-serif;font-weight:500;text-transform:uppercase;line-height:.98;letter-spacing:.5px}
h3,h4{font-family:"Barlow",Arial,sans-serif;font-weight:600;color:var(--ink);line-height:1.2}
a{color:var(--link);text-decoration:none}
section{position:relative;overflow:hidden}

/* hero */
.hero{height:520px;background:var(--night)}
.hero-visual{position:absolute;inset:0;background:
  radial-gradient(ellipse at 70% 30%,rgba(120,150,190,.35),transparent 55%),
  radial-gradient(ellipse at 20% 80%,rgba(80,100,130,.3),transparent 60%),
  linear-gradient(180deg,#1b2029 0%,#0b0d12 100%)}
.hero h1{position:absolute;left:150px;top:270px;color:#fff;font-size:64px}

/* intro article */
.explainer{height:1960px;padding-top:120px}
.explainer .display{margin-left:380px;font-size:80px;color:var(--ink);width:460px}
.explainer .lead{margin:40px 0 0 380px;width:560px;font-size:14px}
.article{position:relative;margin:60px 0 0 380px;width:600px}
.article::before{content:"";position:absolute;left:-60px;top:0;height:1440px;width:1px;background:var(--rule)}
.article h3{font-size:26px;margin:26px 0 14px}
.article p{margin-bottom:14px}
.article-visual{height:150px;margin:20px 0 24px;background:linear-gradient(135deg,#0f1a2a,#2b4a6e 55%,#0c121b)}

/* monitoring banner */
.monitor{height:380px;background:var(--night);color:#fff}
.monitor-visual{position:absolute;inset:0;background:
  radial-gradient(circle at 72% 60%,rgba(230,130,40,.55),transparent 35%),
  radial-gradient(circle at 80% 40%,rgba(60,110,200,.45),transparent 45%),
  linear-gradient(90deg,#07090d 35%,#131a26)}
.monitor .eyebrow{position:absolute;left:150px;top:72px;font-size:10px;line-height:1.4;letter-spacing:2px;text-transform:uppercase;font-weight:600}
.monitor h2{position:absolute;left:150px;top:96px;font-size:64px;width:600px}
.monitor p{position:absolute;left:150px;top:300px;width:520px;font-size:12px;line-height:1.6;color:#c9ccd2}

/* definition */
.definition{height:460px}
.definition .lead{position:absolute;left:150px;top:80px;width:440px;font-family:"Barlow",Arial,sans-serif;font-size:22px;font-weight:500;color:var(--ink);line-height:1.35}
.definition .body{position:absolute;left:150px;top:220px;width:430px}
.definition .body p{margin-bottom:12px}
.definition-visual{position:absolute;left:610px;top:80px;width:440px;height:230px;background:radial-gradient(circle at 60% 55%,#e58a2c,#6b3a16 35%,#121826 75%)}
.definition .caption{position:absolute;left:610px;top:326px;width:440px}

/* how it works */
.how{height:460px;background:var(--night);color:#c9ccd2}
.how h2{position:absolute;left:150px;top:110px;font-family:"Barlow",Arial,sans-serif;text-transform:none;font-weight:600;font-size:30px;color:#fff;line-height:1.2}
.steps{position:absolute;left:150px;top:200px;width:900px;display:flex;gap:20px}
.step{flex:1;border:1px solid #2a2f38;padding:22px 20px;height:200px;font-size:12px;line-height:1.65}
.step b{display:block;font-family:"Barlow",Arial,sans-serif;font-size:22px;color:#fff;margin-bottom:16px;font-weight:600}

/* features */
.features{height:400px}
.features h3{position:absolute;top:100px;width:100%;text-align:center;font-size:30px}
.feature-list{position:absolute;left:150px;top:200px;width:900px;display:flex;gap:40px}
.feature{flex:1;font-size:12px;line-height:1.6}
.feature svg{display:block;margin-bottom:14px}
.feature strong{color:var(--ink)}

/* why */
.why{height:340px}
.why h3{position:absolute;left:150px;top:60px;width:400px;font-size:30px}
.why .body{position:absolute;left:150px;top:150px;width:420px}
.why .body p{margin-bottom:12px}
.reasons{position:absolute;left:620px;top:40px;width:430px;display:grid;grid-template-columns:repeat(3,1fr);gap:26px 18px}
.reason{display:flex;gap:10px;align-items:flex-start;font-size:11px;line-height:1.45;color:var(--ink)}
.reason svg{flex:none}

/* benefits + form */
.benefits{height:580px}
.benefits h3{position:absolute;left:150px;top:100px;width:380px;font-size:30px}
.benefits .body{position:absolute;left:150px;top:200px;width:420px}
.benefits .body p{margin-bottom:12px}
.contact{position:absolute;left:640px;top:20px;width:410px;height:460px;background:var(--soft);padding:36px 34px}
.contact h4{font-family:"Barlow Condensed",sans-serif;font-weight:500;font-size:32px;text-transform:uppercase;margin-bottom:26px}
.contact label{display:block;font-size:11px;color:var(--ink);margin-bottom:6px}
.contact .field{display:block;width:100%;height:40px;background:#fff;border:1px solid var(--rule);margin-bottom:20px;font:inherit;padding:8px}
.contact textarea.field{height:130px;resize:none}
.contact button{display:block;margin:10px 0 0 auto;width:110px;height:40px;background:var(--accent);border:0;font-family:"Barlow",sans-serif;font-weight:600;font-size:13px;color:var(--ink)}

footer{height:96px;border-top:1px solid var(--rule);text-align:center;font-size:11px;color:var(--muted);padding-top:38px}
</style>
</head>
<body>

<section class="hero">
  <div class="hero-visual" role="img" aria-label="Dark cityscape of glowing digital data"></div>
  <h1>Darknet and<br>dark web</h1>
</section>

<section class="explainer">
  <h2 class="display">What is the darknet / dark web?</h2>
  <p class="lead">This short read is your entrance to the Darknet. Both terms stand for the same concept. To understand the darknet you must first explain <a href="#">The internet</a>.</p>

  <div class="article">
    <h3>What is the internet?</h3>
    <p>The internet is a network of computers that are connected to each other through a global network, made up of computers in the middle that are speak all servers and personal devices across the world.</p>
    <p>Every time you visit a web page, your browser asks a server somewhere for the files that build it. The server answers, the files travel back over many connected machines, and the page appears on your screen in a fraction of a second.</p>
    <div class="article-visual" role="img" aria-label="Illustration of connected computers in a global network"></div>
    <p>Each device on the network has its own address, so requests always know where to go. Search engines index the pages that are public, which is why most of what people use every day can be found within seconds.</p>
    <p>This open and searchable part is often called the surface web. It is only a small share of everything that is online, because many pages sit behind logins, paywalls or private company systems.</p>
    <p>Below the surface sits the deep web: mail boxes, bank accounts and internal tools. These are not hidden for bad reasons, they are simply not meant to be indexed for everyone.</p>
    <h3>So how is the internet different to the darknet?</h3>
    <p>The darknet is a layer of hidden networks built on top of the internet. It can only be reached with special software that routes traffic through several relays so that sender and receiver stay anonymous.</p>
    <p>Unlike the internet, pages are not listed by normal search engines and their addresses are long strings of random characters. Users often find them through forums or word of mouth.</p>
    <div class="article-visual" role="img" aria-label="Illustration of hidden encrypted network layers"></div>
    <p>The special routing hides where a request comes from. Each relay only knows the step before and after it, which makes tracking very hard for providers and authorities.</p>
    <p>Journalists, activists and people in restrictive countries use this privacy for good reasons. At the same time, it attracts markets for stolen data, leaked passwords and illegal goods.</p>
    <h3>Is the darknet illegal?</h3>
    <p>Using the darknet is not illegal in most countries. The software itself is legal and freely available. What matters is what you do there: buying or selling stolen data, weapons or drugs remains a crime.</p>
    <p>For companies the darknet is mainly a risk. Leaked credentials, customer records and internal files often end up for sale there long before anyone notices the breach.</p>
    <p>That is why many organisations now watch the darknet closely, so they can react quickly when their information appears.</p>
  </div>
</section>

<section class="monitor">
  <div class="monitor-visual" role="img" aria-label="Abstract swirl of glowing data streams in blue and orange"></div>
  <span class="eyebrow">Darknet monitoring</span>
  <h2>Why and how<br>can the darknet<br>be monitored?</h2>
  <p>The dark web can be a scary place. Especially if you're new to it and are not properly secured with all you need to stay safe.</p>
</section>

<section class="definition">
  <p class="lead">Dark web monitoring refers to the process by which you can search, track, or monitor the information regarding your organization on the dark web.</p>
  <div class="body">
    <p>With the right tools on the dark web, you can track your stolen or leaked information such as intellectual property, compromised passwords, breached credentials and other sensitive data.</p>
    <p>Monitoring services scan hidden forums, markets and paste sites around the clock and alert you as soon as a match for your company is found.</p>
  </div>
  <div class="definition-visual" role="img" aria-label="Glowing orange digital tunnel of data"></div>
  <p class="caption">A mix of automated crawlers and human analysts keeps watch on places where criminals trade data, so you can respond before damage spreads.</p>
</section>

<section class="how">
  <h2>How does dark web<br>monitoring work?</h2>
  <div class="steps">
    <div class="step"><b>01</b>Tools crawl hidden sites and forums and collect new posts, listings and leaks as they appear online.</div>
    <div class="step"><b>02</b>Millions of records are matched against your domains, email addresses, brand names and key staff.</div>
    <div class="step"><b>03</b>When a match is found, the finding is checked and rated by risk, so false alarms are removed early.</div>
    <div class="step"><b>04</b>Your team receives a clear alert with advice on next steps, such as resetting passwords or closing gaps.</div>
  </div>
</section>

<section class="features">
  <h3>Features found in dark web monitoring</h3>
  <div class="feature-list">
    <div class="feature">
      <svg width="40" height="40" viewBox="0 0 40 40" fill="none" stroke="#14161b" stroke-width="1.6"><circle cx="20" cy="20" r="5"/><circle cx="6" cy="8" r="3"/><circle cx="34" cy="8" r="3"/><circle cx="6" cy="32" r="3"/><circle cx="34" cy="32" r="3"/><path d="M8.5 10l7.5 6.5M31.5 10l-7.5 6.5M8.5 30l7.5-6.5M31.5 30l-7.5-6.5"/></svg>
      <strong>Threat intelligence:</strong> When the darknet monitoring service records data matching the search terms. It is then analysed and placed in context for your security team.
    </div>
    <div class="feature">
      <svg width="40" height="40" viewBox="0 0 40 40" fill="none" stroke="#14161b" stroke-width="1.6"><circle cx="17" cy="17" r="11"/><path d="M25 25l10 10"/><path d="M12 17h10M17 12v10"/></svg>
      <strong>Threat hunting:</strong> Hunters look for risks that are not yet detected by other tools and trace them back to their source before attackers can act on them.
    </div>
    <div class="feature">
      <svg width="40" height="40" viewBox="0 0 40 40" fill="none" stroke="#14161b" stroke-width="1.6"><path d="M20 4l13 5v10c0 9-6 15-13 17C13 34 7 28 7 19V9z"/><path d="M14 20l4 4 8-8"/></svg>
      <strong>Quicker incident response:</strong> With quicker responses to indicators of threat and danger, teams contain incidents faster and limit the impact.
    </div>
  </div>
</section>

<section class="why">
  <h3>Why should you use dark web monitoring?</h3>
  <div class="body">
    <p>On the dark web, there are all kinds of things to worry about. Stolen data, leaked files and passwords are traded every day, often without the owner knowing.</p>
    <p>Using dark web monitoring helps you find this information early, protect your clients and staff and meet legal duties around data protection.</p>
  </div>
  <div class="reasons">
    <div class="reason"><svg width="28" height="28" viewBox="0 0 28 28" fill="none" stroke="#14161b" stroke-width="1.5"><rect x="4" y="4" width="20" height="20" rx="2"/><path d="M9 14h10"/></svg>Data stored in unknown places</div>
    <div class="reason"><svg width="28" height="28" viewBox="0 0 28 28" fill="none" stroke="#14161b" stroke-width="1.5"><circle cx="14" cy="10" r="5"/><path d="M5 24c1-5 5-7 9-7s8 2 9 7"/></svg>Third party breaches</div>
    <div class="reason"><svg width="28" height="28" viewBox="0 0 28 28" fill="none" stroke="#14161b" stroke-width="1.5"><rect x="5" y="12" width="18" height="12" rx="2"/><path d="M9 12V8a5 5 0 0110 0v4"/></svg>PHP leaks</div>
    <div class="reason"><svg width="28" height="28" viewBox="0 0 28 28" fill="none" stroke="#14161b" stroke-width="1.5"><path d="M14 3l10 4v7c0 6-4 10-10 11C8 24 4 20 4 14V7z"/></svg>Brand abuse</div>
    <div class="reason"><svg width="28" height="28" viewBox="0 0 28 28" fill="none" stroke="#14161b" stroke-width="1.5"><circle cx="14" cy="14" r="10"/><path d="M14 8v6l4 3"/></svg>Accessing data</div>
    <div class="reason"><svg width="28" height="28" viewBox="0 0 28 28" fill="none" stroke="#14161b" stroke-width="1.5"><path d="M4 22l7-7 5 5 8-10"/><path d="M18 10h6v6"/></svg>Domain spoofing</div>
    <div class="reason"><svg width="28" height="28" viewBox="0 0 28 28" fill="none" stroke="#14161b" stroke-width="1.5"><rect x="4" y="6" width="20" height="16" rx="2"/><path d="M4 8l10 7 10-7"/></svg>Impersonation</div>
    <div class="reason"><svg width="28" height="28" viewBox="0 0 28 28" fill="none" stroke="#14161b" stroke-width="1.5"><path d="M14 4l11 19H3z"/><path d="M14 11v6M14 20v1"/></svg>Malicious threats</div>
  </div>
</section>

<section class="benefits">
  <h3>Benefits of dark web monitoring</h3>
  <div class="body">
    <p>Dark web monitoring offers you with the ability to know where leaks and breaches of sensitive data are coming from, so you can act before attackers use them against you.</p>
    <p>It also shows how your company is seen in criminal circles, which services are targeted and which staff accounts need better protection.</p>
    <p>With early alerts, your team saves time and money, reduces legal risk and keeps the trust of clients and partners who rely on you to handle their data with care.</p>
  </div>
  <form class="contact">
    <h4>Want to know more?</h4>
    <label for="email">Your email</label>
    <input class="field" id="email" type="email">
    <label for="message">Message</label>
    <textarea class="field" id="message"></textarea>
    <button type="submit">Submit</button>
  </form>
</section>

<footer>Copyright © 2023 Velorimo - Cyber Threat Intelligence - Darknet and dark web - All Rights Reserved</footer>

</body>
</html>
```